New Generation Winery needs inspiring label for special bottling

We are a family owned winery in the Rhine Valley in Germany. Check www.brendel-aumann.de . We have a very exciting project going: In 2014 we harvested our best vinyard and split the grapes in half. First half I have treated the way I have done it over the past 40 years. Second half I gave to my daughter who is just entering the winemaking business. She has treated it in a completely different way - her way - the way of the new generation. One of the differentiators; she has squeezed the juices with her bare feet which reduces acidity and bitterness in the wine (less tannins). This is why we want to call the wine "Mondgrüße" (meaning "Moongreets"). Please be careful when writing the "ß" . It is a German letter which replaces the "double s". It is NOT a capital B!! I Have attached a file which gives you the size of the label and another file which shows the current design of the winery labels. If possible it should pick up some elements from the current design (maybe just the colours?) but otherwise you are free. It will go on a dark green bottle, almost black. Apart from the word "Mondgrüße" you need to place the grape "Riesling", the word "trocken" (means dry) and the year of the harvest "2014".

Industry/Entity Type

Brendel

Requirements
Nice to have
• Update 25.3.2015: Have a look at the attached image "Inspiration". Maybe that is a good thought starter, too. Have fun..

```html
<!DOCTYPE html>
<html lang="de">
<head>
<meta charset="utf-8">
<title>Mondgrüße – Riesling 2014 Trocken</title>
<link rel="stylesheet" href="https://fonts.googleapis.com/css2?family=Alegreya:wght@700&family=Cormorant+Garamond:wght@500&display=swap">
<style>
  :root {
    --paper: #f3f2f1;
    --paper-grain: #e6e4e2;
    --wine-deep: #6e0a14;
    --wine: #b3141f;
    --wine-soft: #e8a9ad;
    --blush: #f7e6e6;
    --grape-purple: #3f2a55;
    --grape-red: #9a2f44;
    --grape-gold: #d8d472;
    --title-fill: #ffffff;
    --title-edge: #1a1414;
    --label-ink: #6b0f17;
    --logo-ink: #f6eeea;
  }
  * { margin: 0; padding: 0; box-sizing: border-box; }
  html, body { width: 846px; height: 1200px; overflow: hidden; background: var(--paper); }
  .label {
    position: relative;
    width: 846px;
    height: 1200px;
    overflow: hidden;
    background:
      radial-gradient(circle at 30% 70%, var(--paper) 0, var(--paper-grain) 140%),
      var(--paper);
  }
  .harvest-scene {
    position: absolute;
    left: 8px; top: 8px;
    width: 824px; height: 547px;
    background: linear-gradient(180deg, var(--blush) 0%, var(--wine-soft) 22%, var(--wine) 52%, var(--wine-deep) 78%, var(--wine) 100%);
  }
  .footprint {
    position: absolute;
    left: 95px; top: 500px;
    width: 240px; height: 410px;
    border-radius: 48% 52% 45% 55% / 40% 40% 60% 60%;
    background: radial-gradient(ellipse at 50% 45%, #a8121c 0%, rgba(179,20,31,.75) 45%, rgba(220,90,100,0) 72%);
    filter: blur(6px);
  }
  .grape-cluster {
    position: absolute;
    left: 360px; top: 465px;
    width: 445px; height: 390px;
    border-radius: 48% 52% 40% 60% / 45% 40% 60% 55%;
    background:
      radial-gradient(ellipse at 78% 28%, var(--grape-gold) 0%, rgba(216,212,114,.9) 22%, rgba(216,212,114,0) 42%),
      radial-gradient(ellipse at 48% 38%, var(--grape-purple) 0%, rgba(63,42,85,.85) 25%, rgba(63,42,85,0) 48%),
      radial-gradient(ellipse at 35% 60%, var(--grape-red) 0%, rgba(154,47,68,.8) 40%, rgba(154,47,68,0) 70%);
  }
  .brand-name {
    position: absolute;
    left: 0; right: 0; top: 372px;
    text-align: center;
    font-family: "Cormorant Garamond", serif;
    font-weight: 500;
    font-size: 40px;
    letter-spacing: 1px;
    color: var(--logo-ink);
  }
  .wine-title {
    position: absolute;
    left: 0; right: 0; top: 676px;
    text-align: center;
    font-family: "Alegreya", serif;
    font-weight: 700;
    font-size: 132px;
    line-height: 1;
    color: var(--title-fill);
    -webkit-text-stroke: 2px var(--title-edge);
    text-shadow: 3px 3px 0 var(--title-edge), 0 6px 14px rgba(0,0,0,.35);
  }
  .wine-details {
    position: absolute;
    left: 38px; right: 48px; top: 1118px;
    display: flex;
    justify-content: space-between;
    font-family: "Cormorant Garamond", serif;
    font-weight: 500;
    font-size: 40px;
    letter-spacing: 2px;
    font-variant-numeric: lining-nums;
    color: var(--label-ink);
  }
  .base-rule {
    position: absolute;
    left: 0; right: 0; bottom: 6px;
    height: 2px;
    background: var(--title-edge);
  }
</style>
</head>
<body>
  <main class="label">
    <div class="harvest-scene" role="img" aria-label="Photo of bare feet treading grapes in a wooden barrel, tinted in red"></div>
    <div class="footprint" role="img" aria-label="Red wine footprint"></div>
    <div class="grape-cluster" role="img" aria-label="Illustration of red, purple and golden grape bunches"></div>
    <div class="brand-name">BRENDEL-AUMANN</div>
    <h1 class="wine-title">Mondgrüße</h1>
    <div class="wine-details">
      <span class="grape-variety">RIESLING</span>
      <span class="vintage">2014</span>
      <span class="style">TROCKEN</span>
    </div>
    <div class="base-rule"></div>
  </main>
</body>
</html>
```